Redesign criminal justice consulting website

We run a small professional services firm that does research, evaluation, consulting, and training on criminal justice issues. We need to redesign our website (www.rvmetrics.com). The existing site is something we made ourselves. It is unprofessional and does not do a good job of communicating what we do or who we are.

We would like the new site to provide a basic overview of what we do. Moreover, we would like it to communicate several themes that represent who we are:

* global

* innovative

* analytical

* practical

We view the principal design challenge as figuring out a subtle, interesting, and graphically appealing way to communicate these themes.

Target Market(s)

Our primary customers are governments, research firms, criminal justice agencies, and schools. The people who we want to find our site are seeking research, evaluation, training, or consulting services related to crime, criminal justice, or policing.

Industry/Entity Type

Consulting

Number of Pages Required

2 pages

Requirements
Must have
• 1. We would like the site to use our logo. It is attached (please use the maroon 4-color version with the company name but without the slogan). The site should also use the colors present in our logo. It may use other colors as well, as long as these colors coordinate with the logo colors.

• 2. For main pages or buttons, we need the following:
• *Home
• *About RVM
• *Services
• *E-Training
• *Resources
• *Contact RVM

• 3. We like simple, crisp, subtle designs over "busier," cluttered, or very complex designs.

• 4. We'd like to receive, at a minimum, the home page and a sample inner page.
Nice to have
• We need some help in thinking through what regions or sections should exist on the home page. We are thinking about having a window on there where we can make announcements about recent developments like new reports, new e-training videos, new photographs, etc... We are open to suggestions here.
Should not have
• 1. Gimmicky or overused clipart.
• 2. Cliched images associated with criminal justice, including magnifying glasses, scales of justice, etc... Our logo makes a subtle nod to criminal justice through the use of a fingerprint as the dot on the "J" in the company initials. That''s sufficient for our purposes. Concentrate instead on the themes listed above.
• 3. Major use of colors that don't match our logo, like blue.

```html
<!DOCTYPE html>
<html lang="en">
<head>
<meta charset="utf-8">
<title>RVM — Research &amp; Verity Metrics</title>
<link rel="stylesheet" href="https://fonts.googleapis.com/css2?family=Vollkorn:wght@400;600;700&family=Arimo:wght@400&display=swap">
<style>
:root{
  --maroon:#8e1a1f;
  --brown-top:#86594b;
  --cream:#f7f3e6;
  --olive:#a7935c;
  --olive-dark:#7d6c3e;
  --olive-light:#c1ae78;
  --drop:#6f5f34;
  --panel:#e2d8b0;
  --panel-line:#cbbd8e;
  --rust:#6b2516;
  --orange:#c4672f;
  --orange-text:#b8552a;
  --gold-text:#f2d78f;
  --ink:#222;
  --muted:#8a7d66;
  --link:#c0472a;
  --blue-link:#3a6ea8;
  --footer-text:#f3ead2;
  --footer-mark:#5f5233;
}
*{box-sizing:border-box;margin:0;padding:0}
html,body{width:1139px;height:1200px;overflow:hidden;background:#fff}
body{position:relative;font-family:"Arimo",Arial,sans-serif;color:var(--ink)}
.abs{position:absolute}

.topbar{left:0;top:0;width:1139px;height:10px;background:var(--brown-top)}
.header{left:0;top:10px;width:1139px;height:125px;background:repeating-linear-gradient(135deg,#f4efdc 0 2px,#fbf8ee 2px 5px)}
.brand{left:72px;top:38px;display:flex;align-items:center;gap:12px}
.brand-dot{width:20px;height:20px;border-radius:50%;background:var(--maroon);flex:none}
.brand-name{font-family:"Vollkorn",Georgia,serif;font-weight:700;font-size:60px;line-height:1;color:var(--maroon);white-space:nowrap}
.brand-full{font-family:"Vollkorn",Georgia,serif;font-weight:700;font-size:15px;line-height:1.2;color:var(--maroon);letter-spacing:1px;border-top:1px solid #aaa;border-bottom:1px solid #aaa;padding:4px 0;text-transform:uppercase;white-space:nowrap}
.call{left:800px;top:42px;display:flex;gap:12px;align-items:flex-start}
.call-text{font-family:"Vollkorn",Georgia,serif;line-height:1.05}
.call-label{font-size:25px;color:#7a7060}
.call-number{font-size:28px;color:var(--maroon)}

.nav{left:0;top:135px;width:1139px;height:52px;background:linear-gradient(#b8a46e,#9d8a52);border-bottom:1px solid #6f5f34;display:flex;padding-left:69px}
.nav a{display:flex;align-items:center;justify-content:center;height:52px;font-family:"Vollkorn",Georgia,serif;font-size:21px;color:#fff;text-decoration:none;border-left:1px solid #8c7a45;box-shadow:inset 1px 0 #c7b684}
.nav a:last-child{border-right:1px solid #8c7a45}
.dropdown{left:231px;top:187px;width:179px;background:var(--drop);z-index:3}
.dropdown a{display:block;height:40px;line-height:40px;padding-left:14px;font-family:"Vollkorn",Georgia,serif;font-size:16px;color:#f4ecd4;text-decoration:none;border-bottom:1px solid #857447}

.hero{left:70px;top:207px;width:662px;height:329px;background:linear-gradient(135deg,#b7c3cc 0%,#8f9ba5 35%,#4b4640 65%,#1e1b18 100%)}
.hero-dots{right:0;top:234px;width:124px;height:31px;background:rgba(60,60,60,.75);display:flex;justify-content:space-around;align-items:center;color:#fff;font-size:22px}
.hero-caption{left:0;bottom:0;width:662px;height:70px;background:rgba(0,0,0,.72);padding:8px 12px}
.hero-title{font-family:"Vollkorn",Georgia,serif;font-size:26px;color:#fff;display:flex;align-items:center;gap:12px}
.hero-text{font-size:12px;color:#eee;margin-top:6px}

.search{left:751px;top:207px;width:273px;height:38px;border:1px solid #c9c9c9;font-size:16px;color:#aaa;padding:8px 9px}
.search-btn{left:1030px;top:207px;width:40px;height:38px;background:var(--maroon);display:flex;align-items:center;justify-content:center}
.adv{left:751px;top:252px;font-size:11px;color:var(--blue-link)}

.explore{left:751px;top:288px;width:319px;height:149px;background:linear-gradient(#dccd93,#cdbb7c)}
.explore-globe{left:19px;top:79px;width:115px;height:70px;border-radius:58px 58px 0 0;background:radial-gradient(circle at 50% 80%,#d9cc9c,#b4a370)}
.explore-head{left:10px;top:4px;font-family:"Vollkorn",Georgia,serif;color:var(--maroon);line-height:1}
.explore-head .a{font-size:30px}.explore-head .b{font-size:19px}
.explore-head .c{display:block;font-size:38px}
.explore-list{left:152px;top:12px;border-left:1px solid #b8a56d;padding-left:11px;height:132px;font-family:"Vollkorn",Georgia,serif;font-size:14.5px;color:#6a5a3a;line-height:1}
.explore-list li{list-style:none;margin-bottom:14px}

.videos-head{left:751px;top:460px;width:318px;height:54px;background:var(--orange);border-bottom:3px solid #d8925e;font-family:"Vollkorn",Georgia,serif;font-size:32px;color:var(--gold-text);padding:6px 13px}
.video-title{left:751px;top:528px;font-family:"Vollkorn",Georgia,serif;font-size:19px;color:#2c1a10}
.video-text{left:751px;top:560px;width:320px;font-size:12px;line-height:19px;height:38px;overflow:hidden}
.video{left:751px;top:610px;width:319px;height:239px;background:linear-gradient(160deg,#d7dde0,#a9b1b4 50%,#6f7578)}
.video-play{left:127px;top:95px;width:68px;height:46px;border-radius:6px;background:linear-gradient(#9c9c9c,#5b5b5b);border:1px solid #ddd;display:flex;align-items:center;justify-content:center}
.video-bar{left:751px;top:849px;width:319px;height:24px;background:linear-gradient(#f2f2f2,#cfcfcf);border:1px solid #aaa;font-size:10px;display:flex;align-items:center;gap:8px;padding:0 6px}
.track{width:118px;height:7px;border-radius:4px;background:#bbb;border:1px solid #999}
.video-links{left:751px;top:876px;width:320px}
.video-links li{list-style:none;font-family:"Vollkorn",Georgia,serif;font-size:19px;color:var(--orange-text);height:35px;line-height:34px;border-bottom:1px solid #ddd;white-space:nowrap}

.news{left:70px;top:558px;width:661px;height:463px;background:var(--panel)}
.news-head{height:57px;background:repeating-linear-gradient(135deg,#6f2717 0 2px,#66220f 2px 4px);border-bottom:3px solid #8a3b22;font-family:"Vollkorn",Georgia,serif;font-size:32px;color:var(--gold-text);padding:6px 15px}
.news-item{margin:0 15px 0 14px;padding:8px 0 10px;height:108px;border-bottom:1px solid var(--panel-line)}
.news-item h3{font-family:"Vollkorn",Georgia,serif;font-weight:400;font-size:19px;color:#2c1a10}
.news-date{font-size:11px;color:var(--muted);margin-top:2px}
.news-text{font-size:12px;margin-top:4px;white-space:nowrap;overflow:hidden}
.news-more{font-size:11px;color:var(--link);margin-top:13px}
.news-links{display:flex;padding:14px 16px 0}
.news-links p{width:320px;font-family:"Vollkorn",Georgia,serif;font-size:19px;line-height:29px;color:var(--orange-text);white-space:nowrap}

.footer{left:0;top:1074px;width:1139px;height:126px;background:linear-gradient(#a99463,#8c7848)}
.footer-brand{left:127px;top:20px;gap:9px}
.footer-brand .brand-name{color:var(--footer-mark);font-size:44px}
.footer-brand .brand-full{color:var(--footer-mark);font-size:11.5px;letter-spacing:.8px;border-color:#6e6140;padding:3px 0}
.footer-brand .brand-dot{background:var(--footer-mark);width:14px;height:14px}
.copyright{left:80px;top:100px;font-size:9px;color:#e8dcbc;letter-spacing:.4px;white-space:nowrap}
.footer-divider{left:411px;top:12px;width:1px;height:98px;background:#6f6038}
.footer-nav{left:440px;top:95px;display:flex;font-size:12px;color:var(--footer-text);letter-spacing:.3px}
.footer-nav span.sep{margin:0 27px}
</style>
</head>
<body>
<div class="abs topbar"></div>
<header class="abs header">
  <div class="abs brand">
    <span class="brand-dot"></span>
    <span class="brand-name">RVM</span>
    <span class="brand-full">Research &amp; Verity<br>Metrics</span>
  </div>
  <div class="abs call">
    <svg width="22" height="44" viewBox="0 0 22 44" aria-hidden="true"><rect x="7" y="0" width="3" height="8" fill="#333"/><rect x="1" y="7" width="20" height="36" rx="3" fill="#2a2a2a"/><rect x="4" y="11" width="14" height="10" fill="#8a9a88"/><g fill="#ddd"><rect x="4" y="24" width="3" height="3"/><rect x="9" y="24" width="3" height="3"/><rect x="14" y="24" width="3" height="3"/><rect x="4" y="29" width="3" height="3"/><rect x="9" y="29" width="3" height="3"/><rect x="14" y="29" width="3" height="3"/><rect x="4" y="34" width="3" height="3"/><rect x="9" y="34" width="3" height="3"/><rect x="14" y="34" width="3" height="3"/></g></svg>
    <div class="call-text"><div class="call-label">Call today</div><div class="call-number">555 014 2290</div></div>
  </div>
</header>

<nav class="abs nav">
  <a style="width:161px">Home</a>
  <a style="width:132px">About</a>
  <a style="width:163px">Services</a>
  <a style="width:186px">E-traning</a>
  <a style="width:189px">Resources</a>
  <a style="width:168px">Contact</a>
</nav>
<div class="abs dropdown"><a>Option1</a><a>Option 3</a></div>

<section class="abs hero" role="img" aria-label="Photo of a consultant presenting to colleagues at a flip chart">
  <div class="abs hero-dots"><span>+</span><span>+</span><span style="opacity:.5">+</span><span>+</span></div>
  <div class="abs hero-caption">
    <div class="hero-title"><svg width="22" height="16" viewBox="0 0 22 16" aria-hidden="true"><rect x="0" y="3" width="22" height="13" rx="2" fill="#ccc"/><rect x="3" y="0" width="7" height="4" fill="#ccc"/><circle cx="12" cy="9.5" r="4" fill="#333"/></svg>Lorem ipsum dolor sit amet</div>
    <div class="hero-text">Consectetur adipiscing elit. Nunc quis velit nisi. Nunc mi libero, gravida in elementum non, adipiscing et leo.</div>
  </div>
</section>

<div class="abs search">Search</div>
<div class="abs search-btn"><svg width="24" height="16" viewBox="0 0 24 16" aria-hidden="true"><path d="M1 8h18M13 2l7 6-7 6" stroke="#e9a38d" stroke-width="3" fill="none"/></svg></div>
<div class="abs adv">Advanced options</div>

<section class="abs explore">
  <div class="abs explore-globe" role="img" aria-label="Illustration of a globe"></div>
  <div class="abs explore-head"><span class="a">Explore</span> <span class="b">our</span><span class="c">services</span></div>
  <ul class="abs explore-list">
    <li>Research, Evaluation,<br>&amp; Assessment</li>
    <li>Strategic Planning</li>
    <li>Training</li>
    <li>Technical Assistance</li>
  </ul>
</section>

<div class="abs videos-head">Our videos</div>
<div class="abs video-title">Lorem ipsum dolor sit amet,</div>
<p class="abs video-text">sit amet, consectetur adipiscing elit. Nunc quis velit nisi. Nunc mi libero, gravida in elementum non, adipiscing et</p>
<div class="abs video" role="img" aria-label="Video still of a training class at computers">
  <div class="abs video-play"><svg width="24" height="26" viewBox="0 0 24 26" aria-hidden="true"><path d="M2 1l21 12L2 25z" fill="#222"/></svg></div>
</div>
<div class="abs video-bar">
  <svg width="12" height="12" viewBox="0 0 12 12" aria-hidden="true"><path d="M1 0l11 6-11 6z" fill="#222"/></svg>
  <span class="track"></span>
  <span style="margin-left:14px">00:06 / 10:14</span>
</div>
<ul class="abs video-links">
  <li>Lorem ipsum dolor sit amet,</li>
  <li>Consectetur adipiscing elit. Nunc quis</li>
  <li>Nunc mi libero, gravida in elementum</li>
  <li>Non, adipiscing et leo.</li>
</ul>

<section class="abs news">
  <div class="news-head">More news</div>
  <article class="news-item"><h3>Lorem ipsum dolor</h3><div class="news-date">Wed, 9 - Dic - 2009</div><p class="news-text">sit amet, consectetur adipiscing elit. Nunc quis velit nisi. Nunc mi libero, gravida in elementum non, adipiscing</p><div class="news-more">See more</div></article>
  <article class="news-item"><h3>Lorem ipsum dolor</h3><div class="news-date">Wed, 9 - Dic - 2009</div><p class="news-text">sit amet, consectetur adipiscing elit. Nunc quis velit nisi. Nunc mi libero, gravida in elementum non, adipiscing</p><div class="news-more">See more</div></article>
  <article class="news-item"><h3>Lorem ipsum dolor</h3><div class="news-date">Wed, 9 - Dic - 2009</div><p class="news-text">sit amet, consectetur adipiscing elit. Nunc quis velit nisi. Nunc mi libero, gravida in elementum non, adipiscing</p><div class="news-more">See more</div></article>
  <div class="news-links">
    <p>Estibulum lectus arcu, iaculis vel<br>Proin imperdiet justo et metus</p>
    <p>Estibulum lectus arcu, iaculis vel<br>Proin imperdiet justo et metus</p>
  </div>
</section>

<footer class="abs footer">
  <div class="abs brand footer-brand">
    <span class="brand-dot"></span>
    <span class="brand-name">RVM</span>
    <span class="brand-full">Research &amp; Verity<br>Metrics</span>
  </div>
  <div class="abs copyright">Copyright 2009, Research &amp; Verity Metrics, Inc. All Rights Reserved</div>
  <div class="abs footer-divider"></div>
  <div class="abs footer-nav">
    <span>HOME</span><span class="sep">-</span><span>ABOUT</span><span class="sep">-</span><span>SERVICES</span><span class="sep">-</span><span>E-TRANING</span><span class="sep">-</span><span>RESOURCES</span><span class="sep">-</span><span>CONTACT</span>
  </div>
</footer>
</body>
</html>
```